Smart, Classy, Conservative looking Legal Letterhead

I need a letterhead that when you look at it it "says to you " this is a well established law firm with very smart lawyers, which will one day be appearing before the Supreme Court of the USA. All information about the Law firm should appear at the top of the page. please no information in the footer.

Industry/Entity Type

Legal

Requirements
Must have
• The name of the law firm, both addresses, phone number and fax,, The names of the attorneys, the website.
• Fields that get changed such as the date, VIA, Address of who the letter is going to,
• Re, Index,
• should have a clean neat look, sleek
Nice to have
• some color would be nice. A logo of some sort could be nice as well. Maybe a single S or interlocking P's For Pelworth and Pelworth.
Should not have
• not too modern looking.

```html
<!DOCTYPE html>
<html lang="en">
<head>
<meta charset="utf-8">
<title>Pelworth and Pelworth Law Firm – Letterhead</title>
<link href="https://fonts.googleapis.com/css2?family=Arimo:wght@400;700&display=swap" rel="stylesheet">
<style>
  :root {
    --green: #b8d65a;
    --green-dark: #8db53c;
    --green-pale: #dcebb0;
    --ink: #3b3b3b;
    --ink-soft: #555555;
    --rule-dash: #c9c9c9;
    --paper: #ffffff;
  }
  * { margin: 0; padding: 0; box-sizing: border-box; }
  html, body { width: 925px; height: 1200px; overflow: hidden; background: var(--paper); }
  body { font-family: "Arimo", Arial, sans-serif; color: var(--ink-soft); }
  .letterhead { position: relative; width: 925px; height: 1200px; }
  .abs { position: absolute; white-space: nowrap; }

  .brand-square { position: absolute; left: 54px; top: 68px; width: 96px; height: 96px; background: var(--green); }
  .brand-name { position: absolute; left: 30px; top: 214px; width: 144px; text-align: center; font-size: 15px; line-height: 19px; color: var(--green-dark); font-weight: 400; }

  .firm-name { left: 211px; top: 62px; font-size: 22px; font-weight: 700; color: var(--ink); letter-spacing: 0.2px; }
  .recipient { left: 211px; top: 97px; font-size: 14.5px; line-height: 20.4px; color: var(--ink-soft); }

  .label { font-size: 13px; font-weight: 700; color: var(--ink); letter-spacing: 0.3px; }
  .value { font-size: 14px; color: var(--ink-soft); }

  .contact-label { left: 209px; top: 218px; }
  .phone-icon { left: 208px; top: 241px; }
  .phone-text { left: 241px; top: 241px; }
  .fax-icon { left: 372px; top: 238px; }
  .fax-text { left: 404px; top: 241px; }

  .attorneys-label { left: 211px; top: 286px; }
  .attorneys-list { left: 211px; top: 308px; line-height: 20.4px; }
  .attorneys-bar { position: absolute; left: 343px; top: 308px; width: 3px; height: 39px; background: var(--green); }
  .globe-icon { left: 358px; top: 313px; }
  .website { left: 389px; top: 314px; }

  .meta-rule { position: absolute; left: 596px; top: 186px; width: 1px; height: 160px; background: var(--green-pale); }
  .date-label { left: 620px; top: 183px; }
  .date-value { left: 620px; top: 206px; }
  .via-label { left: 620px; top: 236px; }
  .via-value { left: 620px; top: 256px; }
  .address-label { left: 620px; top: 287px; }
  .address-value { left: 620px; top: 307px; line-height: 20.4px; }

  .band { position: absolute; left: 0; width: 925px; height: 5px; background: var(--green); }
  .hairline { position: absolute; left: 0; width: 925px; height: 1px; background: var(--green-pale); }

  .ref-label { left: 211px; font-size: 17px; font-weight: 700; color: var(--ink); }
  .ref-line { position: absolute; left: 276px; width: 450px; border-top: 1.5px dashed var(--rule-dash); }

  .letter-body { position: absolute; left: 211px; top: 558px; width: 560px; font-size: 16px; line-height: 20.4px; color: var(--ink-soft); }
  .letter-body p { margin-bottom: 19px; }
</style>
</head>
<body>
<div class="letterhead">

  <div class="brand-square" aria-hidden="true"></div>
  <div class="brand-name">Pelworth &amp;<br>Pelworth</div>

  <div class="abs firm-name">PELWORTH AND PELWORTH LAW FIRM</div>
  <div class="abs recipient">
    Hon. Fake Judge Name Here<br>
    United States District Court, E.D.N.Y.<br>
    240 Courthouse Row<br>
    Courtroom XXXXX<br>
    Marlow Heights, NY 11790-2215
  </div>

  <div class="abs label contact-label">REACH US @:</div>
  <svg class="abs phone-icon" width="24" height="18" viewBox="0 0 24 18" aria-hidden="true">
    <path d="M1 6 Q12 -1 23 6 L21 9 L17 8 L17 6 Q12 4 7 6 L7 8 L3 9 Z" fill="var(--ink)"/>
    <path d="M6 9 L18 9 L21 17 L3 17 Z" fill="var(--ink)"/>
    <circle cx="12" cy="13" r="2.2" fill="var(--paper)"/>
  </svg>
  <div class="abs value phone-text">(555) 201-4870</div>
  <svg class="abs fax-icon" width="24" height="22" viewBox="0 0 24 22" aria-hidden="true">
    <rect x="6" y="1" width="12" height="8" fill="none" stroke="var(--ink)" stroke-width="1.6"/>
    <rect x="1" y="8" width="22" height="13" rx="1.5" fill="var(--ink)"/>
    <rect x="4" y="11" width="9" height="3" fill="var(--paper)"/>
    <g fill="var(--paper)">
      <rect x="15" y="11" width="2" height="2"/><rect x="19" y="11" width="2" height="2"/>
      <rect x="15" y="15" width="2" height="2"/><rect x="19" y="15" width="2" height="2"/>
    </g>
  </svg>
  <div class="abs value fax-text">(555) 201-4871</div>

  <div class="abs label attorneys-label">ATTORNEYS:</div>
  <div class="abs value attorneys-list">Daniel A. Pelworth<br>Daniel A. Pelworth</div>
  <div class="attorneys-bar" aria-hidden="true"></div>
  <svg class="abs globe-icon" width="22" height="22" viewBox="0 0 22 22" aria-hidden="true">
    <g fill="none" stroke="var(--ink-soft)" stroke-width="1.3">
      <circle cx="11" cy="11" r="9.5"/>
      <ellipse cx="11" cy="11" rx="4.2" ry="9.5"/>
      <line x1="1.5" y1="11" x2="20.5" y2="11"/>
      <path d="M3 6 H19 M3 16 H19"/>
    </g>
  </svg>
  <div class="abs value website">www.pelworthlaw.com</div>

  <div class="meta-rule" aria-hidden="true"></div>
  <div class="abs label date-label">DATE:</div>
  <div class="abs value date-value">July 4, 2015</div>
  <div class="abs label via-label">VIA:</div>
  <div class="abs value via-value">XXXXXXXX</div>
  <div class="abs label address-label">ADDRESS:</div>
  <div class="abs value address-value">1820 Harbor Lane, Crestwater<br>Beach, FL 32190</div>

  <div class="band" style="top:379px"></div>
  <div class="hairline" style="top:388px"></div>

  <div class="abs ref-label" style="top:410px">Re:</div>
  <div class="ref-line" style="top:425px"></div>
  <div class="abs ref-label" style="top:441px">Index:</div>
  <div class="ref-line" style="top:456px"></div>

  <div class="hairline" style="top:494px"></div>

  <div class="letter-body">
    <p>Your Honor:</p>
    <p>Pursuant to Your Honor’s Individual Practices Rule III(C)(3), enclosed please find a courtesy copy of Plaintiff’s Revised Yadda Yadda Yadda.</p>
    <p>Respectfully,</p>
    <p>Daniel A. Pelworth</p>
  </div>

  <div class="band" style="top:1148px"></div>
  <div class="hairline" style="top:1158px"></div>
</div>
</body>
</html>
```